Website for software company "velbra"

We need a website for our software company/startup named "velbra". We are developing several products (currently 3 standard-software products) which are all in different sectors, but all our products are available for Laptops/PC/Mobile Phones/Tablets, ... We do also create custom software and support our customers with consulting to optimize their processes.
We already have a Logo which you can find in the attached files.
We are a young team of 4 members (two founders and 2 employees).

To get an idea of our products -> the first one is a planning software for healthcare organizations (eg. Mercyway, firebrigade, pharmacy), the second one is a booking software for sport clubs and the third one is a competition software for sports hunting. You see very diverse. Include or ignore this info of our products as you like.

The design has to be a bootstrap 4 (or higher) design. We have licenced FontAwesome as iconset. Responsive design should come without saying.

Coding

Coded - Design and coding required

Number of Pages Required

5+ page

Font styles to use
Sans Serif

Requirements
Must have
• Starting page, product pages, news section, contact, team, services

```html
<!DOCTYPE html>
<html lang="en">
<head>
<meta charset="utf-8">
<title>velbra — Building Powerful Software</title>
<link href="https://fonts.googleapis.com/css2?family=Inter:wght@400;500;600;700&display=swap" rel="stylesheet">
<style>
:root{
  --orange:#f47b30;
  --orange-soft:#fde9db;
  --peach:#fdf2ea;
  --ink:#1f1f1f;
  --muted:#7a7a7a;
  --faint:#b9b9b9;
  --grey-band:#f4f4f6;
  --dark:#2f2f31;
  --line:#e6e6e6;
}
*{box-sizing:border-box;margin:0;padding:0}
html,body{width:1200px;height:4444px;overflow:hidden}
body{font-family:"Inter",sans-serif;color:var(--ink);background:#fff;position:relative}
.abs{position:absolute}
.label{color:var(--orange);font-size:15px;letter-spacing:.3px;text-transform:uppercase}
.h2{font-size:32px;font-weight:600;line-height:1.35}
.btn{display:inline-block;background:var(--orange);color:#fff;font-size:15px;font-weight:500;padding:13px 29px;border-radius:2px}
.brand{display:flex;align-items:center;gap:10px;font-size:38px;font-weight:700;color:var(--ink);letter-spacing:-.5px}
.brand i{width:14px;height:14px;background:var(--orange);display:block}

/* header + hero */
.hero{position:absolute;left:0;top:0;width:1200px;height:600px;background:var(--peach);overflow:hidden}
.hero-shape{position:absolute;inset:0}
.nav{position:absolute;top:20px;left:90px;right:86px;display:flex;justify-content:space-between;align-items:center}
.nav ul{display:flex;list-style:none;gap:48px;align-items:center;font-size:15px}
.nav .contact{border:1px solid var(--orange);padding:10px 20px;border-radius:2px}
.hero h1{position:absolute;left:90px;top:174px;font-size:46px;font-weight:700;line-height:1.27;letter-spacing:.2px;white-space:nowrap;color:var(--ink)}
.hero h1 .accent{color:var(--orange);font-weight:500}
.hero .sub{position:absolute;left:92px;top:316px;font-size:20px}
.hero .btn{position:absolute;left:90px;top:372px}
.follow{position:absolute;left:92px;top:511px;display:flex;align-items:center;gap:14px;font-size:14px;color:var(--muted)}
.follow .bar{width:52px;height:1px;background:var(--faint)}
.follow .dot{width:10px;height:10px;border-radius:50%;background:#555}
.hero-visual{position:absolute;left:668px;top:170px;width:502px;height:316px;border-radius:10px;background:linear-gradient(135deg,#fafbff,#dfe6f4 60%,#c9ced8);box-shadow:0 14px 30px rgba(0,0,0,.12)}
.hero-card{position:absolute;left:522px;top:298px;width:260px;height:150px;border-radius:4px;background:linear-gradient(135deg,#ffffff,#eef1f7);box-shadow:0 10px 24px rgba(0,0,0,.12)}

/* services */
.services .label{position:absolute;top:628px;width:100%;text-align:center}
.services .h2{position:absolute;top:656px;width:100%;text-align:center}
.card{position:absolute;width:264px;height:294px;background:#fff;box-shadow:0 4px 16px rgba(0,0,0,.06);padding:30px 24px}
.card .ico{width:46px;height:46px;border-radius:8px}
.card h3{margin-top:22px;font-size:16px;font-weight:600;line-height:1.4;text-transform:uppercase;min-height:46px}
.card p{margin-top:16px;font-size:13px;line-height:1.55;color:var(--faint)}
.card .more{position:absolute;left:24px;bottom:20px;font-size:13px;font-weight:500}
.card .arrow{position:absolute;right:14px;bottom:16px;width:22px;height:22px}
.card.active .more{color:var(--orange)}
.card.active .corner{position:absolute;right:0;bottom:0;width:0;height:0;border-left:44px solid transparent;border-bottom:44px solid var(--orange)}

/* about */
.about{position:absolute;left:0;top:1491px;width:1200px;height:500px;background:var(--grey-band)}
.about-art{position:absolute;left:22px;top:80px;width:640px;height:400px;background:radial-gradient(ellipse at 45% 40%,#e3e3e6,#f4f4f6 70%)}
.about .txt{position:absolute;left:698px;top:60px;width:420px}
.about .h2{margin-top:8px}
.about p{font-size:13px;line-height:1.6;color:#666;margin-top:22px}
.about .btn{margin-top:30px}

/* team */
.team .label{position:absolute;top:2072px;width:100%;text-align:center}
.team .h2{position:absolute;top:2100px;width:100%;text-align:center}
.member{position:absolute;top:2191px;width:236px;height:272px;background:#fff;box-shadow:0 4px 14px rgba(0,0,0,.06);text-align:center}
.member .photo{height:206px;background:linear-gradient(180deg,#f1f1f1,#dcdcdc)}
.member h4{margin-top:14px;font-size:17px;font-weight:600}
.member small{display:block;font-size:12px;color:#666;margin-top:3px}
.member.active{background:var(--orange);color:#fff}
.member.active small{color:#fff}
.member .soc{position:absolute;right:16px;top:20px;display:flex;flex-direction:column;gap:12px}
.member .soc b{width:10px;height:10px;border-radius:50%;background:#555;display:block}

/* portfolio */
.portfolio{position:absolute;left:0;top:2583px;width:1200px;height:590px;background:linear-gradient(180deg,#fde3cf 0%,#fdf1e7 70%,#fff 100%)}
.portfolio .label{position:absolute;left:90px;top:98px}
.portfolio .h2{position:absolute;left:90px;top:118px;font-size:31px}
.pager{position:absolute;left:776px;top:119px;display:flex;align-items:center;gap:16px;font-size:14px;color:var(--muted)}
.pager .bar{width:56px;height:1px;background:var(--orange)}
.pager .next{color:var(--orange)}
.portfolio .btn{position:absolute;left:998px;top:106px;padding:10px 26px}
.shot{position:absolute;width:334px;height:190px}

/* tech */
.tech .label{position:absolute;top:3266px;width:100%;text-align:center}
.tech .h2{position:absolute;top:3292px;width:100%;text-align:center}
.tech p{position:absolute;top:3340px;left:280px;width:640px;text-align:center;font-size:13px;line-height:1.6;color:#555}
.node{position:absolute;border-radius:50%;background:#fff;box-shadow:0 6px 16px rgba(0,0,0,.08);display:flex;align-items:center;justify-content:center}
.node b{display:block;border-radius:50%}

/* cta */
.cta{position:absolute;left:0;top:3724px;width:1200px;height:342px;background:var(--dark);overflow:hidden;color:#fff;text-align:center}
.cta-art{position:absolute;left:0;top:56px;width:270px;height:240px;background:linear-gradient(135deg,#3c4d72,#1e2a44);transform:skewY(6deg)}
.cta h2{position:absolute;top:96px;width:100%;font-size:32px;font-weight:600}
.cta p{position:absolute;top:148px;left:296px;width:608px;font-size:13px;line-height:1.6}
.cta .btn{position:absolute;left:518px;top:224px}

/* footer */
.footer .brand{position:absolute;left:90px;top:4130px}
.subscribe{position:absolute;left:90px;top:4196px;width:312px;height:40px;border:1px solid var(--line);display:flex;justify-content:space-between;align-items:center;font-size:12px;color:var(--faint);padding-left:16px}
.subscribe span{width:42px;height:40px;background:var(--orange);display:flex;align-items:center;justify-content:center}
.fsoc{position:absolute;left:90px;top:4262px;display:flex;gap:14px}
.fsoc b{width:32px;height:32px;border-radius:50%;background:#f2f2f2;display:block;position:relative}
.fsoc b::after{content:"";position:absolute;left:12px;top:12px;width:8px;height:8px;border-radius:50%;background:#333}
.fcol{position:absolute;top:4142px}
.fcol h5{font-size:18px;font-weight:600;margin-bottom:16px}
.fcol li{list-style:none;font-size:14px;color:var(--muted);line-height:28.5px}
.copy{position:absolute;left:90px;top:4402px;font-size:11px}
.copy span{color:var(--orange);text-decoration:underline}
.totop{position:absolute;left:1069px;top:4342px;width:40px;height:40px;border-radius:50%;background:var(--orange);display:flex;align-items:center;justify-content:center}
</style>
</head>
<body>

<section class="hero">
  <svg class="hero-shape" width="1200" height="600" viewBox="0 0 1200 600">
    <polygon points="0,600 1200,470 1200,600" fill="#fff"/>
    <polygon points="380,240 520,300 380,390" fill="#f6e3d5" opacity=".7"/>
    <polygon points="700,0 980,0 820,150" fill="#fbe5d6" opacity=".6"/>
  </svg>
  <nav class="nav">
    <div class="brand"><i></i>velbra</div>
    <ul>
      <li>Home</li><li>Services</li><li>Team</li><li>Our Works</li>
      <li class="contact">Contact Us</li>
    </ul>
  </nav>
  <h1>BUILDING <span class="accent">POWERFUL</span><br>SOFTWARE</h1>
  <div class="sub">Transforming Ideas Into Solutions</div>
  <span class="btn">Start A Project</span>
  <div class="follow">FOLLOW US <span class="bar"></span><span class="dot"></span><span class="dot"></span><span class="dot"></span></div>
  <div class="hero-visual" role="img" aria-label="Laptop displaying a software dashboard with charts and a world map"></div>
  <div class="hero-card" role="img" aria-label="Floating card with a downloads line chart"></div>
</section>

<section class="services">
  <div class="label">Our Services</div>
  <div class="h2">Trusted Software Development<br>Company</div>

  <div class="card" style="left:178px;top:771px">
    <div class="ico" style="background:linear-gradient(135deg,#f7a23b,#e8413c 55%,#2f6fe0)"></div>
    <h3>Product Design</h3>
    <p>Lorem ipsum dolor sit amet, consectetur adipiscing elit. Cras lacus, velit ridiculus elementum</p>
    <span class="more">READ MORE</span>
    <svg class="arrow" viewBox="0 0 22 22"><path d="M9 7l5 4-5 4z" fill="#222"/></svg>
  </div>
  <div class="card active" style="left:467px;top:771px">
    <div class="ico" style="background:#3d8ef0"></div>
    <h3>Web Development</h3>
    <p>Lorem ipsum dolor sit amet, consectetur adipiscing elit. Cras lacus, velit ridiculus elementum</p>
    <span class="more">READ MORE</span>
    <span class="corner"></span>
  </div>
  <div class="card" style="left:758px;top:771px">
    <div class="ico" style="background:linear-gradient(90deg,#ef4f6c 50%,#8e4fd8 50%);border-radius:6px;height:22px"></div>
    <div class="ico" style="background:linear-gradient(90deg,#3fbf5c 50%,#f5a623 50%);border-radius:6px;height:22px;margin-top:2px"></div>
    <h3 style="margin-top:22px">App Development &amp; Integration</h3>
    <p>Lorem ipsum dolor sit amet, consectetur adipiscing elit. Cras lacus, velit ridiculus elementum</p>
    <span class="more">READ MORE</span>
    <svg class="arrow" viewBox="0 0 22 22"><path d="M9 7l5 4-5 4z" fill="#222"/></svg>
  </div>
  <div class="card" style="left:178px;top:1093px">
    <div class="ico" style="background:radial-gradient(circle,#f5b82e 40%,#555 42%);border-radius:50%"></div>
    <h3>Project Management</h3>
    <p>Lorem ipsum dolor sit amet, consectetur adipiscing elit. Cras lacus, velit ridiculus elementum</p>
    <span class="more">READ MORE</span>
    <svg class="arrow" viewBox="0 0 22 22"><path d="M9 7l5 4-5 4z" fill="#222"/></svg>
  </div>
  <div class="card" style="left:467px;top:1093px">
    <div class="ico" style="background:radial-gradient(circle at 50% 40%,#4da3ec 55%,#f47b30 57%);border-radius:50%"></div>
    <h3>Security &amp; Privacy</h3>
    <p>Lorem ipsum dolor sit amet, consectetur adipiscing elit. Cras lacus, velit ridiculus elementum</p>
    <span class="more">READ MORE</span>
    <svg class="arrow" viewBox="0 0 22 22"><path d="M9 7l5 4-5 4z" fill="#222"/></svg>
  </div>
  <div class="card" style="left:758px;top:1093px">
    <div class="ico" style="background:linear-gradient(135deg,#f5a623 0 33%,#3fbf5c 33% 66%,#e8413c 66%)"></div>
    <h3>Enterprise Solutions</h3>
    <p>Lorem ipsum dolor sit amet, consectetur adipiscing elit. Cras lacus, velit ridiculus elementum</p>
    <span class="more">READ MORE</span>
    <svg class="arrow" viewBox="0 0 22 22"><path d="M9 7l5 4-5 4z" fill="#222"/></svg>
  </div>
</section>

<section class="about">
  <div class="about-art" role="img" aria-label="Isometric illustration of a smartphone with an app menu connected to screen wireframes by a dashed path"></div>
  <div class="txt">
    <div class="label">About Us</div>
    <div class="h2">Company Development<br>Depends On Software</div>
    <p>Lorem Ipsum Dolor Sit Amet, Consectetur Adipiscing Elit. Cras Lacus, Velit Ridiculus Elementum. Facilisi Ipsum, Scelerisque Sapien Vitae, Quis Faucibus.</p>
    <p style="margin-top:16px">Facilisis Lectus Lacus Aliquam Sem Lectus Massa Hac Odio Tristique. Sagittis Ut Sed Neque Odio.Leo Habitant Sollicitudin Dui Nullam Nullam Sapien Praesent. Commodo Scelerisque Varius Cras Curabitur Augue Aliquam Risus.</p>
    <span class="btn">Learn More</span>
  </div>
</section>

<section class="team">
  <div class="label">Our Teams</div>
  <div class="h2">Meet Our Team</div>
  <div class="member" style="left:90px">
    <div class="photo" role="img" aria-label="Portrait photo of team member"></div>
    <h4>Daniel Hart</h4><small>Founder</small>
  </div>
  <div class="member active" style="left:352px">
    <div class="photo" role="img" aria-label="Portrait photo of team member"></div>
    <div class="soc"><b></b><b></b><b></b></div>
    <h4>Daniel Hart</h4><small>Founder</small>
  </div>
  <div class="member" style="left:613px">
    <div class="photo" role="img" aria-label="Portrait photo of team member"></div>
    <h4>Daniel Hart</h4><small>Full-Stuck Development</small>
  </div>
  <div class="member" style="left:874px">
    <div class="photo" role="img" aria-label="Portrait photo of team member"></div>
    <h4>Daniel Hart</h4><small>Full-Stuck Development</small>
  </div>
</section>

<section class="portfolio">
  <div class="label">Portfolio</div>
  <div class="h2">Tech Stack</div>
  <div class="pager">PREV <span class="bar"></span> <span class="next">NEXT</span></div>
  <span class="btn">View All</span>
</section>
<div class="shot" style="left:90px;top:2781px;background:linear-gradient(135deg,#d9dde3,#b9c0ca)" role="img" aria-label="Laptop and devices showing website designs"></div>
<div class="shot" style="left:433px;top:2781px;background:linear-gradient(135deg,#ece9e6,#c9c6c2)" role="img" aria-label="Responsive web design shown on desktop, tablet and phone"></div>
<div class="shot" style="left:776px;top:2781px;background:linear-gradient(135deg,#e06a1e,#8a2c0c)" role="img" aria-label="Orange website layout mockup"></div>
<div class="shot" style="left:90px;top:2981px;background:linear-gradient(135deg,#d8ebf7,#8fc4ea)" role="img" aria-label="Desktop monitor with floating website screens"></div>
<div class="shot" style="left:433px;top:2981px;background:linear-gradient(135deg,#f2f2f0,#9fb83a)" role="img" aria-label="Green website on desktop and tablet on a desk"></div>
<div class="shot" style="left:776px;top:2981px;background:linear-gradient(135deg,#f2e9e2,#c8b7a8)" role="img" aria-label="Web design shown on an all-in-one computer"></div>

<section class="tech">
  <div class="label">Our Technologies</div>
  <div class="h2">Tech Stack</div>
  <p>Lorem Ipsum Dolor Sit Amet, Consectetur Adipiscing Elit. Cras Lacus, Velit Ridiculus Elementum. Facilisi Ipsum, Scelerisque Sapien Vitae, Quis Faucibus.</p>
  <svg class="abs" style="left:0;top:3400px" width="1200" height="320" viewBox="0 0 1200 320">
    <path d="M120 320 Q600 -80 1080 320" fill="none" stroke="#ececec" stroke-width="2"/>
    <path d="M250 320 Q600 60 950 320" fill="none" stroke="#f1f1f1" stroke-width="2"/>
  </svg>
  <div class="node" style="left:584px;top:3414px;width:40px;height:40px"><b style="width:18px;height:18px;background:#5bc6e8"></b></div>
  <div class="node" style="left:354px;top:3440px;width:84px;height:84px"><b style="width:34px;height:14px;border-radius:3px;background:#232f3e"></b></div>
  <div class="node" style="left:792px;top:3442px;width:80px;height:80px"><b style="width:36px;height:36px;background:#336791"></b></div>
  <div class="node" style="left:502px;top:3510px;width:44px;height:44px"><b style="width:20px;height:20px;border-radius:4px;background:#c4003b"></b></div>
  <div class="node" style="left:676px;top:3512px;width:44px;height:44px"><b style="width:20px;height:20px;background:#e36b6b"></b></div>
  <div class="node" style="left:190px;top:3556px;width:80px;height:80px"><b style="width:34px;height:34px;border-radius:4px;background:#222"></b></div>
  <div class="node" style="left:920px;top:3548px;width:84px;height:84px"><b style="width:38px;height:30px;border-radius:4px;background:#d82c20"></b></div>
  <div class="node" style="left:340px;top:3578px;width:50px;height:50px"><b style="width:22px;height:24px;border-radius:3px;background:#e44d26"></b></div>
  <div class="node" style="left:808px;top:3574px;width:52px;height:52px"><b style="width:22px;height:22px;background:#222"></b></div>
  <div class="node" style="left:582px;top:3584px;width:46px;height:46px"><b style="width:18px;height:18px;background:#e88b2a"></b></div>
  <div class="node" style="left:440px;top:3602px;width:84px;height:84px"><b style="width:36px;height:40px;border-radius:4px;background:#1572b6"></b></div>
  <div class="node" style="left:696px;top:3604px;width:84px;height:84px"><b style="width:38px;height:38px;background:#3d3f8f"></b></div>
</section>

<section class="cta">
  <svg class="abs" style="right:0;top:0" width="520" height="342" viewBox="0 0 520 342">
    <polygon points="300,0 520,0 520,200" fill="#3a3a3c"/>
    <polygon points="360,120 520,200 440,342" fill="#39393b"/>
  </svg>
  <div class="cta-art" role="img" aria-label="Stacked laptop screens showing web designs"></div>
  <h2>Let’s Start Your Project</h2>
  <p>Facilisis Lectus Lacus Aliquam Sem Lectus Massa Hac Odio Tristique. Sagittis Ut Sed Neque Odio.Leo Habitant Sollicitudin Dui Nullam Nullam Sapien Praesent. Commodo Scelerisque Varius Cras Curabitur Augue Aliquam Risus.</p>
  <span class="btn">Start A Project</span>
</section>

<footer class="footer">
  <div class="brand"><i></i>velbra</div>
  <div class="subscribe">Email here
    <span><svg width="18" height="18" viewBox="0 0 18 18"><path d="M2 8l14-6-6 14-2-6z" fill="#fff"/></svg></span>
  </div>
  <div class="fsoc"><b></b><b></b><b></b></div>
  <div class="fcol" style="left:529px"><h5>Quick Links</h5><ul><li>Home</li><li>Services</li><li>Team</li><li>Our Works</li><li>Contact Us</li></ul></div>
  <div class="fcol" style="left:713px"><h5>Services</h5><ul><li>Product Design</li><li>Web Development</li><li>APP Development &amp; Integration</li><li>Project Management</li><li>Security &amp; Privacy</li><li>Enterprise Solutions</li></ul></div>
  <div class="fcol" style="left:979px"><h5>Legal</h5><ul><li>Support</li><li>Terms &amp; Condition</li><li>Privacy Policy</li></ul></div>
  <div class="totop"><svg width="16" height="16" viewBox="0 0 16 16"><path d="M3 10l5-5 5 5" stroke="#fff" stroke-width="2" fill="none"/></svg></div>
  <div class="copy">©Copyright 2022. <span>velbra</span> | All Rights Reserved</div>
</footer>

</body>
</html>
```